trifold brochure Bright Harbour

We need a new tri fold brochure (A4 folded to DL) for our company Bright Harbour Paramedical Services Pty Ltd. We have just had a new logo created and this is attached.

The main products we are wanting to highlight are:
1. First Aid training
2. Automated External Defibrillators (mainly the Kova Pulse Linear and Kova Pulsepak AEDs)
3. First Aid Kits and Supplies

Our website is www.brightharbr.com.au This website will be redeveloped in the near future,based on the design of the brochure.

We have added a lot of photos here, please feel free to use what you wish and alter as necessary.

Target Market(s)

Businesses, corporations, and sporting groups. We specialise in corporate courses and do very little public first aid training

Industry/Entity Type

Training

Requirements
Must have
• We are different to our main competitors in that all trainers are Professional Paramedics. Files that can be read and altered in Illustrator CS2 or InDesign CS2.
Nice to have
• A tag line - open to suggestions. Information about Sudden Cardiac Arrest (included in word doc)

```html
<!DOCTYPE html>
<html lang="en">
<head>
<meta charset="utf-8">
<title>Bright Harbour Paramedical Services – AEDs, Kits &amp; Courses</title>
<link rel="stylesheet" href="https://fonts.googleapis.com/css2?family=Montserrat:wght@600;700;800&family=Questrial&display=swap">
<style>
:root{
  --red:#d52128;
  --red-deep:#b9151c;
  --ink:#1e1e1e;
  --black:#0d0d0d;
  --paper:#ffffff;
}
*{margin:0;padding:0;box-sizing:border-box}
html,body{width:1200px;height:848px;overflow:hidden;background:var(--paper)}
.brochure{position:relative;width:1200px;height:848px;overflow:hidden;background:var(--paper);font-family:"Questrial",Arial,sans-serif;color:var(--ink)}

.photo{position:absolute}
.photo-trainer{left:0;top:0;width:245px;height:848px;background:linear-gradient(90deg,#b9bfca 0%,#d7dae2 60%,#f3f4f7 100%)}
.photo-linear{left:325px;top:278px;width:165px;height:97px;border-radius:4px;background:linear-gradient(135deg,#dfe9ee,#b9cdd6)}
.photo-pak{left:660px;top:282px;width:135px;height:126px;border-radius:6px;background:linear-gradient(135deg,#f1f2f4,#cfd3d8)}
.photo-kit{left:502px;top:665px;width:298px;height:183px;background:linear-gradient(135deg,#2c58a6 0%,#e9ecef 45%,#f7f7f7 100%)}

.band{position:absolute;display:flex}
.band .key{background:var(--black);height:100%}
.band .bar{height:100%;background:linear-gradient(90deg,var(--red) 0%,var(--red) 70%,rgba(213,33,40,0) 100%);color:#fff;font-family:"Montserrat",Arial,sans-serif;font-weight:800;padding-left:17px;display:flex;align-items:center;white-space:nowrap}
.band-aeds{left:215px;top:25px;height:32px}
.band-aeds .key{width:30px}
.band-aeds .bar{width:530px;font-size:22px}
.band-kits{left:200px;top:690px;height:56px}
.band-kits .key{width:40px}
.band-kits .bar{width:290px;font-size:22px;line-height:25px}

.copy{position:absolute;font-size:12.2px;line-height:12.75px;white-space:nowrap}
.copy span{display:block}
.copy .b{padding-left:12px}
.copy .c{padding-left:22px}
.copy .gap{height:12.75px}

.product-name{position:absolute;font-family:"Montserrat",Arial,sans-serif;font-weight:700;font-size:14.5px;line-height:16px;white-space:nowrap}
.product-name sup{font-size:8px}

.courses{position:absolute;left:800px;top:0;width:400px;height:848px;background:linear-gradient(90deg,var(--red-deep),var(--red) 6%);color:#fff;font-family:"Montserrat",Arial,sans-serif}
.courses > *{position:absolute;left:40px;white-space:nowrap}
.courses .title{top:30px;font-size:24px;font-weight:800;letter-spacing:.3px;line-height:26px}
.courses .head{font-size:13px;font-weight:800;line-height:15px}
.courses .head small{font-size:9.5px}
.courses .code{font-size:9.5px;font-weight:800;line-height:11px}
.courses .text{font-size:10.2px;font-weight:600;line-height:13px}
.courses .text span{display:block}
.courses .list{font-size:10.2px;font-weight:600;line-height:18px;list-style:none}
.courses .list li::before{content:"• "}
</style>
</head>
<body>
<main class="brochure">

  <div class="photo photo-trainer" role="img" aria-label="Smiling trainer in a striped jumper holding an AED unit in its open carry case"></div>

  <header class="band band-aeds"><span class="key"></span><h1 class="bar">AEDS</h1></header>

  <p class="copy" style="left:250px;top:67px">
    <span>Approximately 33,000 Australians die from Sudden Cardiac Arrest every year. Whilst a heart</span>
    <span>attack is the leading cause of Sudden Cardiac Arrest, it is only one of many causes. Sudden</span>
    <span>Cardiac Arrest can strike anyone, of any age and fitness at any time – including children.</span>
    <span>There is overwhelming evidence that early defibrillation with a device such as an Automated</span>
    <span>External Defibrillator (AED) saves lives. The chance survival decreases by 7 – 10% every minute</span>
    <span>that passes before defibrillation from time of collapse. In areas with public access AEDs,</span>
    <span>survival rates have increased from less than 10% to as high as 80%.</span>
    <span>Our solutions include:</span>
    <span class="b">* Accredited Training delivered by Professional Paramedics</span>
    <span class="b">* Obligation free assessment of workplace / venue</span>
    <span class="b">* Ongoing monitoring / maintenance</span>
    <span class="b">* Clinical debrief by paramedics in the event device is deployed</span>
  </p>
  <p class="copy" style="left:250px;top:227px">
    <span>Our solutions ensure your device and personnel are always ready and functional when it is</span>
    <span>needed.</span>
  </p>

  <h2 class="product-name" style="left:250px;top:273px">Kova<sup>®</sup><br>Pulse<br>Linear</h2>
  <div class="photo photo-linear" role="img" aria-label="Kova Pulse Linear AED unit seated in its network docking station"></div>
  <p class="copy" style="left:250px;top:326px">
    <span>A new</span>
    <span>concept of</span>
    <span>use for AED’s.</span>
  </p>
  <p class="copy" style="left:250px;top:372px">
    <span>It is an AED that</span>
    <span>is permanently</span>
    <span>connected to a</span>
    <span>network, available</span>
    <span>in semi-automatic or fully automatic mode.</span>
    <span>All AED’s connected are under full control</span>
    <span>at all times and can be directly managed</span>
    <span>from a central station.</span>
  </p>
  <p class="copy" style="left:250px;top:477px">
    <span>The AED defibrillators can be connected</span>
    <span>to a server by ethernet cables or wireless</span>
    <span>(Wifi). As soon as a device is taken from</span>
    <span>its docking station, or a technical failure is</span>
    <span>detected the information is immediately</span>
    <span>available on the server and an automatic</span>
    <span>alarm / message is sent.</span>
  </p>
  <p class="copy" style="left:250px;top:564px">
    <span class="b">* Early warning capabilities (e.g. if device</span>
    <span class="c">is deployed or has technical failure)</span>
    <span class="b">* Monitors battery levels and self test</span>
    <span class="c">results</span>
    <span class="b">* Ensures device is always ready for use</span>
    <span class="b">* Easy, quick and secure patient data</span>
    <span class="c">tansfer</span>
    <span class="b">* Quick and easy software &amp; protocol</span>
    <span class="c">updates</span>
  </p>

  <h2 class="product-name" style="left:525px;top:273px">Kova<sup>®</sup><br>Pulsepak</h2>
  <div class="photo photo-pak" role="img" aria-label="Kova Pulsepak pocket AED beside a pen for scale"></div>
  <p class="copy" style="left:525px;top:309px">
    <span>The world’s</span>
    <span>first pocket</span>
    <span>defibrillator.</span>
    <span class="gap"></span>
    <span>A Swiss</span>
    <span>Precision</span>
    <span>Masterpiece.</span>
    <span>The new</span>
    <span>external defibrillator</span>
    <span>so small and light that it</span>
    <span>fits in every coat pocket</span>
    <span>and every doctor’s</span>
    <span>bag, and still meets all</span>
    <span>requirements of a modern AED.</span>
  </p>
  <p class="copy" style="left:525px;top:497px">
    <span>Key Advantages:</span>
    <span class="b">* Ultra light - only 490 grams</span>
    <span class="c">(incl. batteries)</span>
    <span class="b">* Ultra small - 133 X 126 X 35 mm</span>
    <span class="c">(l x w x h)</span>
    <span class="b">* High - resolution LCD</span>
    <span class="b">* Biphasic pulsed defibrillation impulse</span>
    <span class="c">(Tidepulse Wave®)</span>
    <span class="b">* Automatic switch to paediatric energy</span>
    <span class="c">level when paediatric pads are</span>
    <span class="c">plugged in.</span>
  </p>

  <header class="band band-kits"><span class="key"></span><h2 class="bar">FIRST AID KITS<br>&amp; EQUIPMENT</h2></header>
  <p class="copy" style="left:250px;top:757px">
    <span>Bright Harbour Paramedical Services supplies</span>
    <span>a range of First Aid Kits and equipment</span>
    <span>suitable for the home, car or workplace.</span>
  </p>
  <div class="photo photo-kit" role="img" aria-label="Blue first response kit bag with dressings, bandages, resuscitation mask and an AED laid out"></div>

  <aside class="courses">
    <h2 class="title">COURSES</h2>

    <h3 class="head" style="top:66px">PERFORM CPR <small>(HLTCPR201A)</small></h3>
    <p class="text" style="top:85px">
      <span>Participants gain the skills and knowledge required to</span>
      <span>perform Cardiopulmonary Resuscitation (CPR) in line with</span>
      <span>the National Resuscitation Council guidelines.</span>
    </p>

    <h3 class="head" style="top:138px">BASIC LIFE SUPPORT <small>(HLTFA201A)</small></h3>
    <p class="text" style="top:157px">
      <span>Frequently known as Level 1 First Aid. Participants are</span>
      <span>introduced to the skills and background knowledge required</span>
      <span>to recognise / respond to life threatening emergencies</span>
      <span>using basic life support techniques until a more qualified</span>
      <span>medically trained person is available.</span>
    </p>

    <h3 class="head" style="top:234px">APPLY FIRST AID <small>(HLTFA301B)</small></h3>
    <p class="text" style="top:253px">
      <span>Also frequently known as level 2 First Aid. This course</span>
      <span>represents the level of First Aid certification required by</span>
      <span>most industries and employers.</span>
    </p>
    <p class="text" style="top:296px">
      <span>Participants develop First Aid skills that may be applied in</span>
      <span>a range of situations, including community and workplace</span>
      <span>settings. This course can be delivered by flexible learning,</span>
      <span>reducing the time your employees are out of the office.</span>
    </p>

    <h3 class="head" style="top:354px">AUTOMATED EXTERNAL DEFIBRILLATION</h3>
    <p class="code" style="top:374px">(21658VIC)</p>
    <p class="text" style="top:388px">
      <span>Participants develop the necessary skills to safely and</span>
      <span>effectively resuscitate a patient in cardiac arrest using a</span>
      <span>Automated External Defibrillator and Cardiopulmonary</span>
      <span>Resuscitation in line with the National Resuscitation</span>
      <span>Council guidelines.</span>
    </p>

    <h3 class="head" style="top:465px;letter-spacing:-.3px">FIRST AID MANAGEMENT OF ANAPHYLAXIS</h3>
    <p class="code" style="top:485px">(21659VIC)</p>
    <p class="text" style="top:500px">
      <span>Participants develop the skills and knowledge to provide</span>
      <span>first aid to a patient suffering from anaphylaxis.</span>
    </p>
    <p class="text" style="top:531px">Course includes:</p>
    <ul class="list" style="top:546px">
      <li>Anaphylaxis Risk Minimisation</li>
      <li>Anaphylaxis Management Plans</li>
      <li>Recognition &amp; Treatment of Anaphylaxis</li>
      <li>Use of AdrenoJect or AutoDose</li>
    </ul>

    <h3 class="head" style="top:626px">FIRST AID FOR PARENTS</h3>
    <p class="text" style="top:646px">
      <span>A brief course encompassing all the “must know” elements</span>
      <span>of first aid for the parents of infants and toddlers.</span>
    </p>
    <p class="text" style="top:677px">Includes:</p>
    <ul class="list" style="top:692px">
      <li>CPR for babies &amp; children</li>
      <li>Choking</li>
      <li>Short of Breath (Asthma, Croup)</li>
    </ul>
    <p class="text" style="top:747px">
      <span>Designed to fit into the busy schedule of new mums &amp; dads,</span>
      <span>whilst not breaking their budget.</span>
    </p>
  </aside>

</main>
</body>
</html>
```